Cantina Brellanto Website

Cantina Brellanto provides home winemakers and vineyards with ultra-premium frozen wine grapes direct from Italy. Cantina Brellanto grapes are highly unique, as they are the only wine grapes available worldwide that are 100% Organic and have the prestigious Italian DOCG certification. We have developed a patented process for flash-freezing wine grapes, right after being picked off of our wines in Italy. This ensures unparalleled quality for the most discerning winemakers around the world.
In addition to its expanding line of premium wine grapes, Cantina Brellanto also imports high-quality winemaking equipment, such as wine vats, pumps, buckets, etc.
We are looking for a professional website designer to redesign www.cantinabrellanto.example. The redesigned website should have a highly-professional, polished look that conveys our premium product, yet is approachable to our target consumer (target consumer notes below). This website should provide a delightful user experience with the right balance of information and cleanness.
Updates

Requirements
Must have
• 1. Homepage
• 2. About Cantina Brellanto
• 3. Products Pages
• a. Collection of Wine Grapes
• b. Winemaking Equipment
• 4. Resources (FAQs, videos, other winemaking tools and information)
• 5. Where to Buy
• 6. News and Events
• 7. Contact Us
• Other Requirements and Design Guidance
• • Reference current website copy as a starting point. Feel free to copywrite, but this is not required.
• • Imagery from current site can be used, and new imagery can be added. Be sure that any new stock photography is authentically Italian (our target consumer will know if this is/is not an Italian vineyard/grape image).
• • Feel free to tweak logo slightly, but it must maintain similar look and color scheme.
• • Must include design and coding
• • Must be cross-OS compatible, including mobile
• • Website must be easy to update in the future (updating copy, adding images, etc.)
• • Site must be linked to social media pages (Cellar Feed, Twitter)
• • Brand Objectives
• o Educate consumers about the merits of Cantina Brellanto products
• o Stir a passion for our products with well placed imagery and copy
• o Compel consumers to learn more about Cantina Brellanto and act to purchase
• o Create a reason for these loyal consumers to visit Cantina Brellanto again and again
• o IMPORTANT: Strike the right balance between having an ultra-premium look, yet also providing enough information for consumers. It is important to understand the target consumer (below).
• • Sites for Inspiration
• o
• Deadline:
• 3 Weeks?
• Target Markets:
• 1. Intermediate and advanced home winemakers looking for high-quality wine grapes (and equipment) that is authentically Italian. These consumers typically are affluent but earthy. They often read Cellarcraft Journal – the #1 magazine for home winemaking.
• 2. Small vineyards that are looking to supplement their inventory with high-quality imported wine grapes.
• Look and Feel:
• • Elegant
• • Serious
• • Mondern/Traditional
• • Personable but Professional
• • Gender Neutral
• • Upmarket
Nice to have
• shopping cart

```html
<!DOCTYPE html>
<html lang="en">
<head>
<meta charset="utf-8">
<title>Cantina Brellanto — Home</title>
<link href="https://fonts.googleapis.com/css2?family=Roboto+Condensed:wght@400;700&family=Source+Sans+3:ital,wght@0,400;0,600;1,400&display=swap" rel="stylesheet">
<style>
:root{
  --wine:#8e1420;
  --wine-dark:#7a0f1a;
  --topbar:#2c2e31;
  --nav-top:#606265;
  --nav-bottom:#4a4c4f;
  --ink:#555;
  --ink-dark:#333;
  --footer:#333436;
  --footer-text:#a9a9a9;
  --white:#fff;
}
*{box-sizing:border-box;margin:0;padding:0}
html,body{width:1200px;height:986px;overflow:hidden;background:var(--white)}
body{position:relative;font-family:"Source Sans 3",sans-serif;color:var(--ink)}
.abs{position:absolute}
.cond{font-family:"Roboto Condensed",sans-serif}

/* header */
.topbar{left:0;top:0;width:1200px;height:54px;background:var(--topbar)}
.navband{left:0;top:54px;width:1200px;height:51px;background:linear-gradient(var(--nav-top),var(--nav-bottom))}
.brand{left:0;top:0;width:310px;height:105px;background:var(--wine)}
.brand-mark{left:226px;top:18px;width:40px;height:40px;border-radius:50%;background:var(--white)}
.brand-name{left:150px;top:80px;width:192px;text-align:center;font-family:"Roboto Condensed",sans-serif;font-weight:700;font-size:11.5px;color:var(--white);letter-spacing:.3px}
.search{left:573px;top:13px;width:215px;height:24px;border:1px solid #555;background:#26282b;font-size:8px;color:#8a8a8a;padding:7px 11px;font-family:"Roboto Condensed",sans-serif}
.search svg{position:absolute;right:6px;top:5px}
.follow{left:817px;top:20px;font-size:12px;color:var(--white)}
.social{top:17px;width:21px;height:21px;border-radius:50%;background:var(--white)}
.nav a{position:absolute;top:74px;transform:translateX(-50%);font-family:"Roboto Condensed",sans-serif;font-size:12px;color:var(--white);text-decoration:none;white-space:nowrap}
.nav-pointer{left:359px;top:99px}

/* hero */
.hero{left:0;top:105px;width:1200px;height:540px;background:
  radial-gradient(ellipse 340px 300px at 880px 290px,#7d8ca0 0%,#4a5a74 45%,transparent 80%),
  radial-gradient(ellipse 300px 240px at 380px 260px,#6f5568 0%,transparent 75%),
  radial-gradient(ellipse 260px 160px at 720px 520px,#836270 0%,transparent 80%),
  linear-gradient(120deg,#1d2645 0%,#2d3454 45%,#27304e 100%)}
.hero h1{left:183px;top:276px;font-family:"Roboto Condensed",sans-serif;font-weight:400;font-size:30px;color:var(--white);letter-spacing:-.2px}
.hero-copy{left:184px;top:325px;width:498px;font-size:12.2px;line-height:19.7px;color:var(--white)}
.order-btn{left:186px;top:425px;width:177px;height:49px;border:1px solid var(--white);color:var(--white);font-family:"Roboto Condensed",sans-serif;font-size:17px;padding:13px 0 0 26px}
.order-btn svg{position:absolute;right:28px;top:19px}
.hero-arrow{top:346px;width:56px;height:56px}

/* content */
.icon-badge{width:42px;height:42px;border-radius:50%;background:var(--wine)}
.icon-badge svg{position:absolute;left:11px;top:11px}
.section-title{font-family:"Roboto Condensed",sans-serif;font-size:19px;color:var(--wine);white-space:nowrap}
.copy{font-size:9.4px;color:var(--ink)}
.thumb{width:135px;height:104px;border:3px solid #d9d9d9}
.btn-dark{height:23px;background:var(--ink-dark);color:var(--white);font-size:9px;text-align:center;line-height:23px}
.avatar{width:34px;height:32px}
.post-name{font-size:9.4px;color:var(--ink-dark)}
.post-date{font-size:9px;font-style:italic;color:var(--ink)}

/* footer */
.footer{left:0;top:918px;width:1200px;height:68px;background:var(--footer)}
.footer-links{left:183px;top:948px;font-size:8.2px;color:var(--footer-text);white-space:nowrap;font-family:"Roboto Condensed",sans-serif}
.footer-links span{margin:0 7px}
.copyright{right:184px;top:948px;font-size:8px;color:var(--footer-text);font-family:"Roboto Condensed",sans-serif}
</style>
</head>
<body>

<header>
  <div class="abs topbar"></div>
  <div class="abs navband"></div>
  <div class="abs brand"></div>
  <div class="abs brand-mark"></div>
  <div class="abs brand-name">CANTINA BRELLANTO</div>

  <div class="abs search">SEARCH :
    <svg width="12" height="12" viewBox="0 0 12 12"><circle cx="5" cy="5" r="3.6" fill="none" stroke="#777" stroke-width="1.5"/><line x1="7.7" y1="7.7" x2="11" y2="11" stroke="#777" stroke-width="1.7"/></svg>
  </div>
  <div class="abs follow cond">FOLLOW US :</div>
  <div class="abs social" style="left:884px" aria-label="Social link one"></div>
  <div class="abs social" style="left:912px" aria-label="Social link two"></div>
  <div class="abs social" style="left:939px" aria-label="Social link three"></div>
  <div class="abs social" style="left:967px" aria-label="Social link four"></div>
  <div class="abs social" style="left:994px" aria-label="News feed"></div>

  <nav class="nav">
    <a style="left:365px">HOME</a>
    <a style="left:452px">ORDER</a>
    <a style="left:549px">ABOUT US</a>
    <a style="left:669px">THE COLLECTION</a>
    <a style="left:800px">NEWS/EVENTS</a>
    <a style="left:900px">FAQ</a>
    <a style="left:988px">CONTACT</a>
  </nav>
  <svg class="abs nav-pointer" width="14" height="7" viewBox="0 0 14 7"><polygon points="0,7 7,0 14,7" fill="#3a3d44"/></svg>
</header>

<section class="abs hero" role="img" aria-label="Close-up of dew-covered dark grapes on the vine with autumn leaves"></section>
<h1 class="abs hero" style="background:none;width:auto;height:auto;left:183px;top:276px">REDEFINING THE ART OF WINEMAKING</h1>
<p class="abs hero-copy">With over 15 years of home and commercial winemaking experience, Cantina Brellanto elevates your winemaking experience with premium Italian grape musts from the heart of Tuscany. Cantina Brellanto brings the Tuscan vineyard to your doorstep, with 5 select varietals that are 100% Organic and DOCG Certified.</p>
<div class="abs order-btn">ORDER NOW
  <svg width="24" height="12" viewBox="0 0 24 12"><line x1="0" y1="6" x2="22" y2="6" stroke="#fff" stroke-width="1.6"/><polyline points="16,1 22,6 16,11" fill="none" stroke="#fff" stroke-width="1.6"/></svg>
</div>
<svg class="abs hero-arrow" style="left:75px" viewBox="0 0 56 56"><circle cx="28" cy="28" r="27" fill="none" stroke="rgba(255,255,255,.35)" stroke-width="2"/><polygon points="17,28 33,18 29,28 33,38" fill="rgba(255,255,255,.35)"/></svg>
<svg class="abs hero-arrow" style="left:1068px" viewBox="0 0 56 56"><circle cx="28" cy="28" r="27" fill="none" stroke="rgba(255,255,255,.35)" stroke-width="2"/><polygon points="39,28 23,18 27,28 23,38" fill="rgba(255,255,255,.35)"/></svg>

<!-- collection -->
<div class="abs icon-badge" style="left:180px;top:672px">
  <svg width="20" height="20" viewBox="0 0 20 20"><circle cx="11" cy="5" r="3" fill="#fff"/><path d="M1 13 Q6 10 10 13 L16 12 Q18 12 17 14 L11 17 Q5 18 1 16Z" fill="#fff"/></svg>
</div>
<h2 class="abs section-title" style="left:231px;top:684px">OUR COLLECTION</h2>
<svg class="abs" style="left:580px;top:686px" width="22" height="9" viewBox="0 0 22 9"><polyline points="5,1 2,4.5 5,8" fill="none" stroke="#888" stroke-width="1.3"/><polyline points="17,1 20,4.5 17,8" fill="none" stroke="#888" stroke-width="1.3"/></svg>
<p class="abs copy" style="left:181px;top:730px;width:420px;line-height:17px">With over 15 years of home and commercial winemaking experience, Cantina Brellanto elevates your winemaking experience with premium Italian grape musts from the heart of Tuscany.</p>
<div class="abs thumb" style="left:180px;top:779px;background:linear-gradient(135deg,#9fbf5a,#3b3d7a 55%,#6f9a3a)" role="img" aria-label="Bunches of purple grapes on the vine"></div>
<div class="abs thumb" style="left:327px;top:779px;background:radial-gradient(circle at 40% 30%,#6b4a30,#2a1a12 70%)" role="img" aria-label="Oak barrels in a dim wine cellar"></div>
<div class="abs thumb" style="left:473px;top:779px;background:radial-gradient(circle at 50% 50%,#3a3e6a,#1a1c33 70%,#b8a24a)" role="img" aria-label="Close-up of a dark grape cluster"></div>

<!-- about -->
<div class="abs icon-badge" style="left:636px;top:667px">
  <svg width="20" height="20" viewBox="0 0 20 20"><circle cx="6" cy="7" r="2.4" fill="#fff"/><circle cx="11" cy="7" r="2.4" fill="#fff"/><circle cx="16" cy="7" r="2.4" fill="#fff"/><circle cx="8.5" cy="11.5" r="2.4" fill="#fff"/><circle cx="13.5" cy="11.5" r="2.4" fill="#fff"/><circle cx="11" cy="16" r="2.4" fill="#fff"/></svg>
</div>
<h2 class="abs section-title" style="left:688px;top:678px">ABOUT US</h2>
<p class="abs copy" style="left:639px;top:728px;width:182px;line-height:15.4px">With over 15 years of home and commercial winemaking experience, Cantina Brellanto elevates your winemaking experience with premium Italian grape musts from the heart of Tuscany.</p>
<p class="abs copy" style="left:639px;top:820px;width:182px;line-height:15.4px">elevates your winemaking experience with premium Italian grape musts...</p>
<div class="abs btn-dark" style="left:639px;top:866px;width:83px">Read More</div>

<!-- social feed -->
<div class="abs icon-badge" style="left:858px;top:666px"></div>
<h2 class="abs" style="left:913px;top:673px;font-family:'Roboto Condensed',sans-serif;font-weight:700;font-size:24px;color:var(--wine)">Cellar Feed</h2>

<div class="abs avatar" style="left:857px;top:728px;background:linear-gradient(#c98f6a,#6a3a2a)" role="img" aria-label="Member avatar"></div>
<div class="abs post-name" style="left:903px;top:730px">Lena Corvaro</div>
<div class="abs post-date" style="left:903px;top:746px">Posted on 27 Aug 2013</div>

<div class="abs avatar" style="left:857px;top:774px;background:linear-gradient(#8fbf4a,#4d7a2a)" role="img" aria-label="Member avatar"></div>
<div class="abs post-name" style="left:903px;top:776px">Lena Corvaro</div>
<div class="abs post-date" style="left:903px;top:791px">Posted on 27 Aug 2013</div>

<div class="abs avatar" style="left:857px;top:819px;background:linear-gradient(#7a6a8a,#3a2f4a)" role="img" aria-label="Grape cluster thumbnail"></div>
<div class="abs post-name" style="left:903px;top:821px">Lena Corvaro</div>
<div class="abs post-date" style="left:903px;top:837px">Posted on 27 Aug 2013</div>

<div class="abs btn-dark" style="left:857px;top:868px;width:83px">View More</div>

<footer>
  <div class="abs footer"></div>
  <div class="abs footer-links">HOME<span>|</span>ORDER<span>|</span>ABOUT US<span>|</span>THE COLLECTION<span>|</span>NEWS/EVENTS<span>|</span>FAQ<span>|</span>CONTACT</div>
  <div class="abs copyright">© COPYRIGHT 2013 CANTINA BRELLANTO. ALL RIGHTS RESERVED.</div>
</footer>

</body>
</html>
```